Yacht, Boats, Watersports company needs a redesign of business card

Hello Designers!
We are a Boat dealership company that sells fun in the water, we sell boats, Yachts, Kayaks and also yacht WaterSport toys. We are looking to redesign our business cards in to something a little bit more sophisticated. in a way that we can make better use of our company colors. I'm attaching a zipped file containing the company 3 sets of company logo which one is an horizontal another one is a vertical and also a chromed 3d logo. Also is included two set of business cards that we use and also some designs that i think it's interesting. We use PMS 2026c Orange and PMS 7687C Blue. I would like to see at least two different options with the orange as accent and also using blue as an accent color. It's really important for the business cards to have a font option and size that is legible to most people. Our current website is wwww.corvellamarine.com. Please visit if you want to have a better feeling of the Boat dealership
You can send Single sided or double side options. We are now using single sided but we may be open for a double side option if we really like the design.
Target Market(s)
Marine, boat sales, yacht sales, water toys sales/
Contact Information for Business Card
Name: Dale Pritchett
Address: 718 West Halden Lane,
Dania Beach, FL 33019
Phone: 954-382-7146
Fax: 954:382-7139
Cell: 954-451-8320
Email: 212@corvellamarine.com
Website: corvellamarine.com
Requirements
Must have
- the current information of the business card provided.
logo
use the PMS Colors
Nice to have
- a touch of elegance and sophistication but simple
Should not have
- should not have any typography that is hard to read, the card should be simple but yet sophisticated.

```html
<!DOCTYPE html>
<html lang="en">
<head>
<meta charset="utf-8">
<title>Corvella Marine – Business Card</title>
<link rel="stylesheet" href="https://fonts.googleapis.com/css2?family=Poppins:wght@400;700&display=swap">
<style>
  :root {
    --backdrop: #3a3939;
    --brand-orange: #e35f2a;
    --orange-light: #ec7a4c;
    --brand-blue: #2b3274;
    --paper: #ffffff;
    --sky-top: #8b7bc8;
    --sky-mid: #c9c3e6;
    --spray: #eceae8;
  }
  * { box-sizing: border-box; margin: 0; padding: 0; }
  html, body {
    width: 1200px; height: 1200px; overflow: hidden;
    background: var(--backdrop);
    font-family: "Poppins", sans-serif;
  }
  .sheet {
    position: relative; width: 1200px; height: 1200px;
    display: flex; flex-direction: column; align-items: center; justify-content: center; gap: 70px;
  }
  .card {
    position: relative; width: 880px; height: 503px;
    border-radius: 20px; overflow: hidden;
    box-shadow: 0 14px 30px rgba(0,0,0,.35);
  }

  /* Front */
  .card-front .photo {
    position: absolute; inset: 0;
    background: linear-gradient(160deg, var(--sky-top) 0%, var(--sky-mid) 30%, var(--spray) 55%, #d7d5d3 100%);
  }
  .front-brand {
    position: absolute; left: 440px; top: 338px;
    display: flex; align-items: center; gap: 14px;
  }
  .brand-dot { width: 52px; height: 52px; border-radius: 50%; background: var(--brand-orange); flex: none; }
  .front-brand .brand-name {
    font-weight: 700; font-size: 26px; letter-spacing: 1px; color: var(--brand-blue); text-transform: uppercase;
  }

  /* Back */
  .card-back { background: var(--brand-orange); }
  .card-back .shape { position: absolute; inset: 0; }
  .back-brand {
    position: absolute; left: 60px; top: 90px; width: 330px;
    display: flex; flex-direction: column; align-items: center; gap: 28px;
  }
  .back-brand .brand-mark {
    width: 230px; height: 230px; border-radius: 50%; background: var(--brand-orange);
  }
  .back-brand .brand-name {
    font-weight: 700; font-size: 30px; letter-spacing: 1.5px; color: var(--brand-blue);
    text-transform: uppercase; white-space: nowrap;
  }
  .contact {
    position: absolute; left: 470px; top: 46px; width: 380px; color: var(--paper);
  }
  .contact .holder-name {
    font-weight: 700; font-size: 40px; line-height: 1.1; text-transform: uppercase; letter-spacing: .5px;
    padding-bottom: 16px; border-bottom: 2px dotted rgba(255,255,255,.85); margin-bottom: 22px;
  }
  .contact-list { list-style: none; display: flex; flex-direction: column; gap: 10px; }
  .contact-list li {
    display: flex; align-items: flex-start; gap: 16px;
    font-size: 21px; line-height: 1.3; font-weight: 400;
  }
  .contact-list svg { width: 22px; height: 22px; flex: none; margin-top: 4px; fill: var(--paper); }
</style>
</head>
<body>
<main class="sheet">

  <section class="card card-front" aria-label="Card front">
    <div class="photo" role="img" aria-label="Photograph of a white cabin motor boat speeding through white spray under a violet sky"></div>
    <div class="front-brand">
      <span class="brand-dot"></span>
      <span class="brand-name">Corvella Marine</span>
    </div>
  </section>

  <section class="card card-back" aria-label="Card back">
    <svg class="shape" viewBox="0 0 880 503" preserveAspectRatio="none" aria-hidden="true">
      <rect width="880" height="503" fill="var(--brand-orange)"/>
      <circle cx="110" cy="300" r="345" fill="var(--orange-light)"/>
      <circle cx="100" cy="310" r="330" fill="var(--paper)"/>
    </svg>

    <div class="back-brand">
      <span class="brand-mark"></span>
      <span class="brand-name">Corvella Marine</span>
    </div>

    <div class="contact">
      <h1 class="holder-name">Dale Pritchett</h1>
      <ul class="contact-list">
        <li>
          <svg viewBox="0 0 24 24"><path d="M6.6 10.8a15 15 0 0 0 6.6 6.6l2.2-2.2a1 1 0 0 1 1-.25 11.4 11.4 0 0 0 3.6.57 1 1 0 0 1 1 1V20a1 1 0 0 1-1 1A17 17 0 0 1 3 4a1 1 0 0 1 1-1h3.5a1 1 0 0 1 1 1c0 1.25.2 2.45.57 3.57a1 1 0 0 1-.25 1z"/></svg>
          <span>954-382-7146</span>
        </li>
        <li>
          <svg viewBox="0 0 24 24"><path d="M12 2a10 10 0 1 0 0 20 10 10 0 0 0 0-20zm6.9 6h-3a15.6 15.6 0 0 0-1.4-3.6A8 8 0 0 1 18.9 8zM12 4a14 14 0 0 1 1.9 4h-3.8A14 14 0 0 1 12 4zM4.3 14a8 8 0 0 1 0-4h3.4a16 16 0 0 0 0 4zm.8 2h3a15.6 15.6 0 0 0 1.4 3.6A8 8 0 0 1 5.1 16zm3-8h-3a8 8 0 0 1 4.4-3.6A15.6 15.6 0 0 0 8.1 8zM12 20a14 14 0 0 1-1.9-4h3.8A14 14 0 0 1 12 20zm2.3-6H9.7a14.7 14.7 0 0 1 0-4h4.6a14.7 14.7 0 0 1 0 4zm.2 5.6a15.6 15.6 0 0 0 1.4-3.6h3a8 8 0 0 1-4.4 3.6zm1.8-5.6a16 16 0 0 0 0-4h3.4a8 8 0 0 1 0 4z"/></svg>
          <span>corvellamarine.com</span>
        </li>
        <li>
          <svg viewBox="0 0 24 24"><path d="M7 2h8l3 3v4H7zM4 10h16a2 2 0 0 1 2 2v8a2 2 0 0 1-2 2H4a2 2 0 0 1-2-2v-8a2 2 0 0 1 2-2zm3 3v2h10v-2zm0 4v2h6v-2z"/></svg>
          <span>954:382-7139</span>
        </li>
        <li>
          <svg viewBox="0 0 24 24"><path d="M8 1h8a2 2 0 0 1 2 2v18a2 2 0 0 1-2 2H8a2 2 0 0 1-2-2V3a2 2 0 0 1 2-2zm0 3v14h8V4zm4 15.2a1.2 1.2 0 1 0 0 2.4 1.2 1.2 0 0 0 0-2.4z"/></svg>
          <span>954-451-8320</span>
        </li>
        <li>
          <svg viewBox="0 0 24 24"><path d="M2 5h20v14H2zm2 2v.5l8 5 8-5V7zm0 2.9V17h16V9.9l-8 5z"/></svg>
          <span>212@corvellamarine.com</span>
        </li>
        <li>
          <svg viewBox="0 0 24 24"><path d="M12 2a7 7 0 0 0-7 7c0 5.2 7 13 7 13s7-7.8 7-13a7 7 0 0 0-7-7zm0 9.5A2.5 2.5 0 1 1 12 6.5a2.5 2.5 0 0 1 0 5z"/></svg>
          <span>718 West Halden Lane,<br>Dania Beach, FL 33019</span>
        </li>
      </ul>
    </div>
  </section>

</main>
</body>
</html>
```